Lumigram Page Design for a Medical Billing Business

We need help designing a lumigram page that is professional, yet friendly that will attract medical practitioners (doctors, therapists, nutritionists, chiropractors, etc) to check out and follow our business. I have attached our logo which must be incorporated in the design.

```html
<!DOCTYPE html>
<html lang="en">
<head>
<meta charset="utf-8">
<title>Lyra Practice Billing – Lumigram Cover</title>
<link rel="stylesheet" href="https://fonts.googleapis.com/css2?family=Poppins:wght@400;600;700&display=swap">
<style>
  :root {
    --pink: #c956a6;
    --purple: #7a56b2;
    --violet-text: #6f50a9;
    --mark: #9a55ae;
    --page: #ffffff;
    --banner-shadow: rgba(0, 0, 0, 0.35);
  }
  * { box-sizing: border-box; margin: 0; padding: 0; }
  html, body {
    width: 1200px; height: 1200px; overflow: hidden;
    background: var(--page);
    font-family: "Poppins", sans-serif;
  }
  .canvas { position: relative; width: 1200px; height: 1200px; }

  .brand-mark {
    position: absolute; top: 150px; left: 0; width: 1200px;
    display: flex; align-items: center; justify-content: center; gap: 18px;
  }
  .brand-mark__dot {
    width: 30px; height: 30px; border-radius: 50%; background: var(--mark);
  }
  .brand-mark__name {
    font-size: 46px; font-weight: 600; color: var(--mark); letter-spacing: 1px;
  }

  .cover {
    position: absolute; left: 60px; top: 402px; width: 1087px; height: 403px;
    box-shadow: 0 0 18px 4px var(--banner-shadow);
    overflow: hidden;
  }
  .cover__backdrop {
    position: absolute; inset: 0;
    background:
      radial-gradient(ellipse 420px 300px at 280px 260px, rgba(240,250,255,0.95), rgba(240,250,255,0) 70%),
      linear-gradient(100deg, #c3d3e8 0%, #d6e5f2 22%, #ecf5fa 45%, #f2f5f8 75%, #f0f2f6 100%);
  }
  .cover__logo {
    position: absolute; right: 26px; top: 60px;
    display: flex; align-items: center; gap: 6px;
  }
  .cover__logo-dot { width: 12px; height: 12px; border-radius: 50%; background: var(--mark); }
  .cover__logo-name { font-size: 20px; font-weight: 600; color: var(--mark); }

  .cover__title {
    position: absolute; top: 108px; left: 0; width: 100%; text-align: center;
    font-size: 47px; font-weight: 600; color: var(--pink); letter-spacing: 0.3px;
  }
  .cover__tagline {
    position: absolute; top: 170px; left: 0; width: 100%; text-align: center;
    font-size: 22px; font-weight: 400; color: var(--violet-text);
  }
  .cover__phone {
    position: absolute; top: 238px; left: 342px;
    display: flex; align-items: center; gap: 14px;
  }
  .cover__phone-icon { width: 38px; height: 38px; }
  .cover__phone-number {
    font-size: 48px; font-weight: 700; color: var(--pink); letter-spacing: 1px;
  }

  .cover__contact {
    position: absolute; top: 360px;
    display: flex; align-items: center; gap: 8px;
    font-size: 20px; color: var(--violet-text);
  }
  .cover__contact--web { left: 30px; }
  .cover__contact--mail { right: 28px; }
  .cover__contact strong { font-weight: 600; }
  .cover__contact-icon { width: 24px; height: 24px; }
</style>
</head>
<body>
<main class="canvas">
  <header class="brand-mark">
    <span class="brand-mark__dot"></span>
    <span class="brand-mark__name">Lyra Practice Billing</span>
  </header>

  <section class="cover">
    <div class="cover__backdrop" role="img" aria-label="Soft blue backdrop with faint DNA helix and molecular hexagon pattern"></div>

    <div class="cover__logo">
      <span class="cover__logo-dot"></span>
      <span class="cover__logo-name">Lyra Practice Billing</span>
    </div>

    <h1 class="cover__title">Lyra Practice Billing, LLC</h1>
    <p class="cover__tagline">Medical billing tailored to your practices needs</p>

    <div class="cover__phone">
      <svg class="cover__phone-icon" viewBox="0 0 38 38" aria-hidden="true">
        <circle cx="19" cy="19" r="19" fill="var(--purple)"/>
        <path d="M13.5 10.5c1-.6 2 .2 2.6 1.2l1.2 2.2c.5 1 .2 1.9-.7 2.5l-.9.6c.8 2.3 2.6 4.3 4.9 5.4l.7-.8c.7-.8 1.7-.9 2.6-.3l2.1 1.4c1 .7 1.5 1.7.8 2.7-1.4 2-3.4 2.8-6 1.6-4.7-2.2-8-6-9.3-10.9-.6-2.3.4-4.5 2-5.6z" fill="#fff"/>
      </svg>
      <span class="cover__phone-number">425-555-0182</span>
    </div>

    <div class="cover__contact cover__contact--web">
      <svg class="cover__contact-icon" viewBox="0 0 24 24" aria-hidden="true">
        <circle cx="12" cy="12" r="12" fill="var(--pink)"/>
        <g fill="none" stroke="#fff" stroke-width="1.2">
          <circle cx="12" cy="12" r="6"/>
          <ellipse cx="12" cy="12" rx="2.6" ry="6"/>
          <path d="M6 12h12M7 9h10M7 15h10"/>
        </g>
      </svg>
      <span>www.<strong>lyrapracticebilling</strong>.com</span>
    </div>

    <div class="cover__contact cover__contact--mail">
      <svg class="cover__contact-icon" viewBox="0 0 24 24" aria-hidden="true">
        <circle cx="12" cy="12" r="12" fill="var(--pink)"/>
        <rect x="6.5" y="8" width="11" height="8" rx="1" fill="none" stroke="#fff" stroke-width="1.3"/>
        <path d="M6.8 8.5 12 12.5l5.2-4" fill="none" stroke="#fff" stroke-width="1.3"/>
      </svg>
      <span>Admin@lyrapracticebilling.com</span>
    </div>
  </section>
</main>
</body>
</html>
```